Sterling Oak Renovations, LLC
Long Island Home Remodeling & Design
Professional
Mark Delvecchi
Owner
42 Harlow Avenue
Brentmoor NY 11893
sterlingoakrenovations@mailbox-demo.com
SterlingOakRenovations-demo.com
I would like two business card done. One with a picture for networking events and one w/o for normal use.
I choose two sides only as an option for the photo on the one version. The photo can be on either side, but I would like to see an example of both.
Sterling Oak Renovations, LLC Logo
Mug Shot

```html
<!DOCTYPE html>
<html lang="en">
<head>
<meta charset="utf-8">
<title>Sterling Oak Renovations, LLC — Stationery</title>
<link rel="stylesheet" href="https://fonts.googleapis.com/css2?family=Roboto:wght@400;700&display=swap">
<style>
  :root{
    --backdrop:#e9e6e1;
    --ink-dark:#0e1a21;
    --ink-mid:#1d2f38;
    --teal:#1b9cbc;
    --teal-deep:#0c5f7a;
    --teal-pale:#cfeaf3;
    --paper:#ffffff;
    --paper-tint:#f1f7fa;
    --text-grey:#4a5a62;
    --photo-a:#c98f6c;
    --photo-b:#6d4a3a;
  }
  *{box-sizing:border-box;margin:0;padding:0}
  html,body{width:1200px;height:619px;overflow:hidden}
  body{background:var(--backdrop);font-family:"Roboto",Arial,sans-serif;position:relative;color:var(--ink-dark)}
  .piece{position:absolute;box-shadow:0 3px 8px rgba(0,0,0,.35)}

  /* logo wordmark */
  .brand{font-weight:700;text-transform:uppercase;letter-spacing:.5px;line-height:1;display:flex;align-items:center;gap:4px;white-space:nowrap}
  .brand .dot{display:inline-block;background:var(--teal);flex:none}
  .brand-light{color:var(--paper)}
  .brand-dark{color:var(--ink-mid)}

  /* business cards */
  .card{width:120px;height:78px;overflow:hidden}
  .card-photo{background:linear-gradient(135deg,var(--ink-dark),var(--ink-mid) 60%,var(--teal-deep));}
  .card-plain{background:linear-gradient(180deg,var(--paper-tint),var(--teal-pale) 55%,var(--teal) 100%)}
  .card .brand{font-size:7px;position:absolute;left:8px;top:10px}
  .card .brand .dot{width:6px;height:6px}
  .card .mug{position:absolute;right:8px;top:18px;width:34px;height:42px;background:linear-gradient(160deg,var(--photo-a),var(--photo-b))}
  .card .contact{position:absolute;left:8px;bottom:9px;font-size:3.6px;line-height:1.45;color:var(--teal-pale);white-space:nowrap}
  .card .contact b{font-size:5px;color:var(--paper)}
  .card-plain .brand{left:0;right:0;top:26px;justify-content:center;font-size:8px}
  .card-plain .tagline{position:absolute;left:0;right:0;top:38px;text-align:center;font-size:3.6px;color:var(--text-grey);white-space:nowrap}
  .card-plain .band{position:absolute;left:0;right:0;bottom:0;height:14px;background:linear-gradient(90deg,var(--ink-dark),var(--teal-deep))}

  .stack .card{width:140px;height:86px}
  .stack .card .mug{width:38px;height:48px}
  .stack .card-plain .brand{top:30px}
  .stack .card-plain .tagline{top:42px}

  /* letter / envelope */
  .envelope-dl{background:var(--paper)}
  .envelope-dl .brand{position:absolute;left:14px;top:16px;font-size:11px}
  .envelope-dl .brand .dot{width:10px;height:10px}
  .envelope-dl .tagline{position:absolute;left:14px;top:30px;font-size:4px;color:var(--text-grey);white-space:nowrap}
  .envelope-dl .recipient{position:absolute;left:160px;top:48px;font-size:5.5px;line-height:1.6;color:var(--ink-mid)}
  .envelope-dl .band{position:absolute;left:0;right:0;bottom:0;height:26px;background:linear-gradient(180deg,var(--teal-pale),var(--teal) 60%,var(--teal-deep))}
  .envelope-dl .band .mark{position:absolute;right:14px;top:6px;width:14px;height:14px;background:var(--ink-mid)}

  .envelope-blue{background:radial-gradient(ellipse at 50% 0%,var(--teal) 0%,var(--teal-deep) 55%,var(--ink-dark) 100%);overflow:hidden}
  .envelope-blue .flap{position:absolute;left:0;top:0;width:100%;height:100%}
  .envelope-blue .brand{position:absolute;left:20px;bottom:40px;font-size:14px;color:rgba(255,255,255,.35)}
  .envelope-blue .brand-top{left:0;right:0;top:74px;bottom:auto;justify-content:center;font-size:8px;color:var(--teal-pale)}

  /* letterhead */
  .letterhead{width:270px;height:480px;background:var(--paper);overflow:hidden}
  .letterhead .header{height:48px;background:linear-gradient(90deg,var(--ink-dark),var(--ink-mid) 60%,var(--teal-deep));position:relative}
  .letterhead .header::after{content:"";position:absolute;left:0;right:0;bottom:-6px;height:6px;background:linear-gradient(90deg,var(--teal-deep),var(--teal),var(--teal-pale))}
  .letterhead .header .brand{position:absolute;left:14px;top:16px;font-size:10px}
  .letterhead .header .brand .dot{width:9px;height:9px}
  .letterhead .header .contact{position:absolute;right:12px;top:10px;font-size:4.2px;line-height:1.5;color:var(--teal-pale);text-align:right;white-space:nowrap}
  .letterhead .watermark{position:absolute;left:0;right:0;top:190px;text-align:center;font-weight:700;font-size:72px;color:#eef1f3;letter-spacing:4px}
  .letterhead .footer{position:absolute;left:0;right:0;bottom:0;height:16px;border-top:2px solid var(--teal);background:var(--paper-tint);font-size:4.5px;color:var(--text-grey);display:flex;align-items:center;padding-left:14px}
  .letterhead .footer .mark{position:absolute;right:12px;top:3px;width:9px;height:9px;background:var(--ink-mid)}
</style>
</head>
<body>

<!-- business cards, top left -->
<div class="piece card card-photo" style="left:60px;top:60px">
  <div class="brand brand-light"><span class="dot"></span>Sterling Oak</div>
  <div class="mug" role="img" aria-label="Portrait photo of the owner"></div>
  <div class="contact"><b>Mark Delvecchi</b><br>Owner<br>42 Harlow Avenue<br>Brentmoor NY 11893</div>
</div>
<div class="piece card card-plain" style="left:60px;top:163px">
  <div class="brand brand-dark"><span class="dot"></span>Sterling Oak</div>
  <div class="tagline">Long Island Home Remodeling &amp; Design</div>
  <div class="band"></div>
</div>

<!-- business card stack, lower left -->
<div class="stack">
  <div class="piece card card-photo" style="left:56px;top:318px;transform:rotate(-8deg)">
    <div class="brand brand-light"><span class="dot"></span>Sterling Oak</div>
    <div class="mug" role="img" aria-label="Portrait photo of the owner"></div>
    <div class="contact"><b>Mark Delvecchi</b><br>Owner<br>SterlingOakRenovations-demo.com</div>
  </div>
  <div class="piece card card-plain" style="left:78px;top:372px;transform:rotate(-5deg)">
    <div class="brand brand-dark"><span class="dot"></span>Sterling Oak</div>
    <div class="tagline">Long Island Home Remodeling &amp; Design</div>
    <div class="band"></div>
  </div>
  <div class="piece card card-photo" style="left:66px;top:430px;transform:rotate(-2deg)">
    <div class="brand brand-light"><span class="dot"></span>Sterling Oak</div>
    <div class="mug" role="img" aria-label="Portrait photo of the owner"></div>
    <div class="contact"><b>Mark Delvecchi</b><br>Owner<br>sterlingoakrenovations@mailbox-demo.com<br>42 Harlow Avenue, Brentmoor NY 11893</div>
  </div>
</div>

<!-- DL envelope, top centre -->
<div class="piece envelope-dl" style="left:283px;top:53px;width:384px;height:187px">
  <div class="brand brand-dark"><span class="dot"></span>Sterling Oak</div>
  <div class="tagline">Long Island Home Remodeling &amp; Design</div>
  <div class="recipient">Mark Delvecchi<br>42 Harlow Avenue<br>Brentmoor NY 11893</div>
  <div class="band"><span class="mark"></span></div>
</div>

<!-- envelopes, lower centre -->
<div class="piece envelope-dl" style="left:283px;top:345px;width:370px;height:108px;transform:rotate(-3deg)">
  <div class="brand brand-dark"><span class="dot"></span>Sterling Oak</div>
  <div class="tagline">Long Island Home Remodeling &amp; Design</div>
</div>
<div class="piece envelope-blue" style="left:312px;top:377px;width:384px;height:182px">
  <svg class="flap" viewBox="0 0 384 182" preserveAspectRatio="none" aria-hidden="true">
    <path d="M0 0 Q192 120 384 0" fill="none" stroke="rgba(255,255,255,.25)" stroke-width="1.5"/>
    <line x1="20" y1="160" x2="364" y2="160" stroke="rgba(255,255,255,.2)" stroke-width="1"/>
  </svg>
  <div class="brand brand-top"><span class="dot" style="width:7px;height:7px"></span>Sterling Oak</div>
  <div class="brand">Sterling Oak Renovations</div>
</div>

<!-- letterheads, right -->
<div class="piece letterhead" style="left:797px;top:36px;height:440px">
  <div class="header">
    <div class="brand brand-light"><span class="dot"></span>Sterling Oak</div>
  </div>
</div>
<div class="piece letterhead" style="left:806px;top:84px">
  <div class="header">
    <div class="brand brand-light"><span class="dot"></span>Sterling Oak</div>
    <div class="contact">42 Harlow Avenue<br>Brentmoor NY 11893<br>sterlingoakrenovations@mailbox-demo.com<br>SterlingOakRenovations-demo.com</div>
  </div>
  <div class="watermark">SOR</div>
  <div class="footer">Long Island Home Remodeling &amp; Design<span class="mark"></span></div>
</div>

</body>
</html>
```